Flyer for an pediatric sleep consultancy - to distribute to play and childcare centers etc.

I need a flyer that will attract the attention of parents with children between the age of babies to toddlers, who may be experiencing sleep issues. The flyer will be placed at places such as community centers, doctors room, play centers, kindergardens, etc.

My company is called "The Quiet Meadow Nest" and provides a sleep consultancy service. My service essentially provides a customized plan for parents to follow and general advice and guidance. It is not medical advice.

I like to the flyer to have an overall tone that is soft and peaceful with a clean and beautiful design, however can catch the attention of parents who may be struggling with their child's sleep issues and are sleep deprived. I would like photos with minimal text. The colour I use is a brownish rose. I will attach some of my designs to give you an idea. You can have a look at my homepage as well to get an idea about my esthetic direction and the colour. Although the colour of my page is a bit too brownish....

I will provide the text to appear in the flyer once I have a better idea of the layout that I prefer for the flyer. The text however wont be extensive, just some catchy points.

I want to direct people to my website which is www.thequietmeadownest.example
I offer a first FREE evaluation call, to the parents, to get to know each other better, learn about their child's particular sleep problems and see if we are a good fit and can work together. I would like to have this information somehow on the flyer, so that the parents will contact me.
I also have a facebook page, which is: The Quiet Meadow Nest

I have a logo that I would like to appear on the flyer. I will attach the file once the uploader on pixel fair is fixed.

When I print the flyer - I like to print A5 SIZE ... please make sure the formatting is OK for this size.

Here are some text ideas. of course all of it would be too much, I guess. On the front of the flyer I would like to have some catchy phrase or something similar to get people interested and to want to know more. On the back there could be a bit more text and information. But I'm open too suggestions....
I'm not too sure about the wording yet. But here are some text that I might be use:

Is sleep an issue in your home?

Is your baby having trouble sleeping? ... are you?!
I can help!

Sleep, baby, sleep….

Teaching children how to sleep

The Quiet Meadow Nest is a pediatric sleep consultancy that specializes in helping parents with children who struggle to develop good and healthy sleep habits.
Disruptive sleep patterns or not enough sleep can affect the physical, mental and emotional development of your child.

Of course nobody plans to have a sleep problem, but habits can become easily ingrained and spiral quickly out of control and you can find yourself sleep deprived, desperate and not too sure what to do. You see all the other sleeping babies and wish there was someone who understood what you were going through?! Well, there is!

Contact me for a free 15 minute consultation.

This 15 minute „mini“ consultation is a chance to discuss your unique sleep challenges and sleep goals with me. I will provide you with an overview of how I will work with your family to achieve your wildest sleep dreams (goals).
Furthermore do I understand and believe that every child and their family is unique and there is no one size fits all!
I would love to have a chat with you and talk about how I can help make things easier for you and your family!

Do I need a sleep consultant for my child?
The answer is yes if:
- if your child will only fall asleep when nursing or bottle feeding
- if your child needs a dummy or other external aid, like being rocked, patted or taken for a care ride to fall asleep
- if your good night routine is a challenging and exhausting procedure instead of a relaxed and enjoyable moment for the whole family
- if sleep is a constant battle in your home which leaves you feeling frustrated and exhausted
- if your own lack of sleep is taking a toll on you and the whole family

What can I do for you?

I will:

- Guide you to set an age appropriate foundation for good sleep
- Create an individual sleep plan tailored especially to your child’s sleep needs and circumstances
- Help you to teach your childto go to sleep and get back to sleep independently during the night
- show you how to teach your child to take healthful, restorative naps
-Learn

Contact:

Marta Lindqvist
info@thequietmeadownest.example
www.thequietmeadownest.example
+34 612 384 570

Consultations in English, German or Spanish via Phone/VidTalk or home consultation

Reason: I have to go on a business trip and won't be able to choose a design until the deadline. During the trip I won't have time to give feedback and ask for changes. thank you

Target Market(s)

parents, sleep deprived mothers, young families, child care provider,

Industry/Entity Type

Baby Care

Contact Information for Business Card

Marta Lindqvist
pediatric sleep consultant
+34 612 384 570

```html
<!DOCTYPE html>
<html lang="en">
<head>
<meta charset="utf-8">
<title>The Quiet Meadow Nest – Flyer</title>
<link rel="stylesheet" href="https://fonts.googleapis.com/css2?family=Lato:wght@300;400;700;900&display=swap">
<style>
  :root {
    --rose: #c4897d;
    --rose-deep: #b5705f;
    --rose-soft: #e9cdc6;
    --ink: #2f2a28;
    --ink-soft: #5a5250;
    --paper: #ffffff;
    --backdrop: #eeeae6;
  }
  * { box-sizing: border-box; margin: 0; padding: 0; }
  html, body { width: 1200px; height: 900px; overflow: hidden; }
  body {
    background: var(--backdrop);
    font-family: "Lato", Arial, sans-serif;
    color: var(--ink);
    position: relative;
  }
  .page {
    position: absolute;
    top: 60px;
    width: 552px;
    height: 783px;
    background: var(--paper);
    overflow: hidden;
    box-shadow: 0 2px 10px rgba(0,0,0,.12);
  }
  .page--front { left: 32px; }
  .page--back { left: 612px; }
  .abs { position: absolute; }
  .decor { position: absolute; inset: 0; width: 100%; height: 100%; }

  /* photo placeholders */
  .photo { position: absolute; }
  .photo--crib {
    left: 0; top: 0; width: 552px; height: 420px;
    background: linear-gradient(180deg, #f3f1f0 0%, #ebe6e4 45%, #f1e4df 75%, #fbf7f5 100%);
  }
  .photo--round {
    border-radius: 50%;
    border: 5px solid var(--paper);
    background: radial-gradient(circle at 45% 45%, #f7e3da 0%, #ead0c5 55%, #d9b6aa 100%);
  }
  .photo--mother { left: 365px; top: 268px; width: 186px; height: 186px; }
  .photo--sleeper { left: 425px; top: 470px; width: 130px; height: 130px; }
  .photo--hands {
    left: 0; top: 560px; width: 165px; height: 223px;
    background: linear-gradient(160deg, #f4ddd2 0%, #efd3c7 50%, #fbf3ef 100%);
  }
  .photo--toddler {
    left: 0; top: 0; width: 553px; height: 232px;
    background: linear-gradient(180deg, #dfe2e5 0%, #eceef0 55%, #f7f7f8 85%, #ffffff 100%);
  }
  .photo--consultant {
    left: 18px; top: 515px; width: 110px; height: 245px;
    background: linear-gradient(180deg, #f0e7df 0%, #d9c9bd 50%, #3e3a3c 100%);
    border-radius: 46px 46px 6px 6px;
  }

  /* brand */
  .brand { position: absolute; display: flex; flex-direction: column; align-items: center; color: var(--ink-soft); }
  .brand__mark { width: 34px; height: 34px; border-radius: 50%; border: 1.5px solid var(--rose); }
  .brand__name { font-weight: 300; white-space: nowrap; }
  .brand--front { left: 126px; top: 38px; width: 300px; }
  .brand--front .brand__mark { width: 54px; height: 54px; margin-bottom: 8px; }
  .brand--front .brand__name { font-size: 23px; }
  .brand--back { left: 150px; top: 655px; width: 190px; }
  .brand--back .brand__mark { margin-bottom: 4px; }
  .brand--back .brand__name { font-size: 14px; }

  /* front headline */
  .hero { position: absolute; left: 36px; top: 372px; color: var(--paper); }
  .hero__title {
    font-weight: 700; font-size: 22px; line-height: 30px; text-transform: uppercase; letter-spacing: .3px;
  }
  .hero__sub {
    margin-top: 12px; font-weight: 700; font-size: 14px; line-height: 18px; text-transform: uppercase; letter-spacing: .3px;
  }
  .hero__lull { margin-top: 10px; font-weight: 300; font-size: 21px; }

  .intro { position: absolute; left: 168px; top: 585px; width: 352px; }
  .intro__title { color: var(--rose-deep); font-weight: 700; font-size: 15.5px; margin-bottom: 6px; }
  .intro p { font-size: 9.6px; line-height: 13px; margin-bottom: 8px; color: var(--ink); }
  .intro__web { position: absolute; left: 170px; top: 752px; font-size: 9.6px; }
  .intro__web span { color: var(--rose-deep); }

  /* back */
  .section { position: absolute; left: 43px; width: 470px; }
  .section__title { color: var(--rose-deep); font-weight: 700; font-size: 14px; margin-bottom: 7px; }
  .section p { font-size: 10.6px; line-height: 14.4px; }
  .section--offer { top: 232px; }
  .section--need { top: 342px; }
  .section--help { top: 506px; left: 120px; width: 400px; }
  .section--help .lead { font-weight: 700; font-size: 11px; margin-bottom: 5px; }
  .checklist { list-style: none; margin-top: 5px; }
  .checklist li {
    position: relative; padding-left: 16px; font-size: 10.6px; line-height: 12.5px; margin-bottom: 6px;
  }
  .checklist li svg { position: absolute; left: 0; top: 1px; width: 11px; height: 11px; }

  .languages { position: absolute; left: 142px; top: 722px; width: 190px; font-size: 9.5px; line-height: 12px; font-weight: 700; color: var(--ink); }
  .contact { position: absolute; left: 345px; top: 666px; }
  .contact__label { font-weight: 700; font-size: 14px; }
  .contact__name { color: var(--rose-deep); font-weight: 700; font-size: 16px; text-transform: uppercase; margin-top: 1px; }
  .contact__line { font-size: 9.8px; line-height: 13px; display: flex; align-items: center; gap: 4px; }
  .contact__line svg { width: 8px; height: 8px; }
  .contact__phone {
    margin-top: 4px; background: var(--rose); color: var(--paper); font-weight: 900; font-size: 17px;
    padding: 2px 6px; display: inline-flex; align-items: center; gap: 6px;
  }
  .contact__phone svg { width: 17px; height: 14px; }
</style>
</head>
<body>

<!-- FRONT -->
<section class="page page--front" aria-label="Flyer front">
  <div class="photo photo--crib" role="img" aria-label="Photo of a newborn sleeping in a white crib"></div>

  <svg class="decor" viewBox="0 0 552 783" aria-hidden="true">
    <path d="M0,0 H130 C70,8 28,30 0,62 Z" fill="var(--rose)"/>
    <path d="M552,0 H430 C490,10 530,40 552,90 Z" fill="var(--rose)"/>
    <path d="M0,372 C40,352 130,360 200,352 C260,345 300,310 345,300 C365,296 380,306 372,330
             C360,380 380,420 410,445 C440,470 440,520 420,548
             C300,560 150,566 0,560 Z" fill="var(--rose)"/>
    <path d="M0,560 C60,600 120,690 165,783 H0 Z" fill="var(--rose)" opacity=".9"/>
  </svg>

  <div class="photo photo--round photo--mother" role="img" aria-label="Photo of a mother resting beside her sleeping baby"></div>
  <div class="photo photo--round photo--sleeper" role="img" aria-label="Photo of a baby sleeping peacefully"></div>
  <div class="photo photo--hands" role="img" aria-label="Photo of a baby hand holding an adult finger"></div>

  <div class="brand brand--front">
    <span class="brand__mark"></span>
    <span class="brand__name">The Quiet Meadow Nest</span>
  </div>

  <div class="hero">
    <h1 class="hero__title">Is sleep an<br>issue in your<br>home?</h1>
    <p class="hero__sub">Is your baby having trouble sleeping?<br>… are you?! I can help!</p>
    <p class="hero__lull">Sleep. baby. sleep….</p>
  </div>

  <div class="intro">
    <h2 class="intro__title">Teaching children how to sleep</h2>
    <p>The Quiet Meadow Nest is a pediatric sleep consultancy that specializes in helping parents with children who struggle to develop good and healthy sleep habits. Disruptive sleep patterns or not enough sleep can affect the physical, mental and emotional development of your child.</p>
    <p>Of course nobody plans to have a sleep problem, but habits can become easily ingrained and spiral quickly out of control and you can find yourself sleep deprived, desperate and not too sure what to do. You see all the other sleeping babies and wish there was someone who understood what you were going through?! Well, there is!</p>
  </div>
  <p class="intro__web">www.<span>thequietmeadownest</span>.example</p>
</section>

<!-- BACK -->
<section class="page page--back" aria-label="Flyer back">
  <div class="photo photo--toddler" role="img" aria-label="Photo of a toddler peeking over a white blanket"></div>

  <svg class="decor" viewBox="0 0 553 783" aria-hidden="true">
    <path d="M553,0 H430 C490,12 535,50 553,110 Z" fill="var(--rose)"/>
    <path d="M0,0 H60 C30,10 10,28 0,48 Z" fill="var(--rose)"/>
    <path d="M0,690 C80,760 250,778 553,770 V783 H0 Z" fill="var(--rose)"/>
    <path d="M0,600 C10,680 60,740 130,783 H0 Z" fill="var(--rose)"/>
  </svg>

  <div class="photo photo--consultant" role="img" aria-label="Photo of the consultant holding a toddler"></div>

  <div class="section section--offer">
    <h2 class="section__title">Contact me for a free 15 minute consultation.</h2>
    <p>This 15 minute „mini“ consultation is a chance to discuss your unique sleep challenges and sleep goals with me. I will provide you with an overview of how I will work with your family to achieve your wildest sleep dreams (goals). Furthermore do I understand and believe that every child and their family is unique and there is no one size fits all! I would love to have a chat with you and talk about how I can help make things easier for you and your family!</p>
  </div>

  <div class="section section--need">
    <h2 class="section__title">Do I need a sleep consultant for my child?</h2>
    <p>The answer is yes if:</p>
    <ul class="checklist">
      <li><svg viewBox="0 0 11 11"><rect x=".5" y=".5" width="10" height="10" fill="none" stroke="var(--rose)"/><path d="M2.5,5.5 L4.5,7.8 L9.5,1.5" fill="none" stroke="var(--rose-deep)" stroke-width="1.5"/></svg>if your child will only fall asleep when nursing or bottle feeding</li>
      <li><svg viewBox="0 0 11 11"><rect x=".5" y=".5" width="10" height="10" fill="none" stroke="var(--rose)"/><path d="M2.5,5.5 L4.5,7.8 L9.5,1.5" fill="none" stroke="var(--rose-deep)" stroke-width="1.5"/></svg>if your child needs a dummy or other external aid, like being rocked, patted or taken for<br>a care ride to fall asleep</li>
      <li><svg viewBox="0 0 11 11"><rect x=".5" y=".5" width="10" height="10" fill="none" stroke="var(--rose)"/><path d="M2.5,5.5 L4.5,7.8 L9.5,1.5" fill="none" stroke="var(--rose-deep)" stroke-width="1.5"/></svg>if your good night routine is a challenging and exhausting procedure instead of a relaxed<br>and enjoyable moment for the whole family</li>
      <li><svg viewBox="0 0 11 11"><rect x=".5" y=".5" width="10" height="10" fill="none" stroke="var(--rose)"/><path d="M2.5,5.5 L4.5,7.8 L9.5,1.5" fill="none" stroke="var(--rose-deep)" stroke-width="1.5"/></svg>if sleep is a constant battle in your home which leaves you feeling frustrated and exhausted</li>
      <li><svg viewBox="0 0 11 11"><rect x=".5" y=".5" width="10" height="10" fill="none" stroke="var(--rose)"/><path d="M2.5,5.5 L4.5,7.8 L9.5,1.5" fill="none" stroke="var(--rose-deep)" stroke-width="1.5"/></svg>if your own lack of sleep is taking a toll on you and the whole family</li>
    </ul>
  </div>

  <div class="section section--help">
    <h2 class="section__title">What can I do for you?</h2>
    <p class="lead">I will :</p>
    <ul class="checklist">
      <li><svg viewBox="0 0 11 11"><rect x=".5" y=".5" width="10" height="10" fill="none" stroke="var(--rose)"/><path d="M2.5,5.5 L4.5,7.8 L9.5,1.5" fill="none" stroke="var(--rose-deep)" stroke-width="1.5"/></svg>Guide you to set an age appropriate foundation for good sleep</li>
      <li><svg viewBox="0 0 11 11"><rect x=".5" y=".5" width="10" height="10" fill="none" stroke="var(--rose)"/><path d="M2.5,5.5 L4.5,7.8 L9.5,1.5" fill="none" stroke="var(--rose-deep)" stroke-width="1.5"/></svg>Create an individual sleep plan tailored especially to your child’s sleep<br>needs and circumstances</li>
      <li><svg viewBox="0 0 11 11"><rect x=".5" y=".5" width="10" height="10" fill="none" stroke="var(--rose)"/><path d="M2.5,5.5 L4.5,7.8 L9.5,1.5" fill="none" stroke="var(--rose-deep)" stroke-width="1.5"/></svg>Help you to teach your childto go to sleep and get back to sleep<br>independently during the night</li>
      <li><svg viewBox="0 0 11 11"><rect x=".5" y=".5" width="10" height="10" fill="none" stroke="var(--rose)"/><path d="M2.5,5.5 L4.5,7.8 L9.5,1.5" fill="none" stroke="var(--rose-deep)" stroke-width="1.5"/></svg>show you how to teach your child to take healthful, restorative naps</li>
      <li><svg viewBox="0 0 11 11"><rect x=".5" y=".5" width="10" height="10" fill="none" stroke="var(--rose)"/><path d="M2.5,5.5 L4.5,7.8 L9.5,1.5" fill="none" stroke="var(--rose-deep)" stroke-width="1.5"/></svg>Learn</li>
    </ul>
  </div>

  <div class="brand brand--back">
    <span class="brand__mark"></span>
    <span class="brand__name">The Quiet Meadow Nest</span>
  </div>
  <p class="languages">Consultations in English, German<br>or Spanish via Phone/VidTalk or home<br>consultation</p>

  <div class="contact">
    <p class="contact__label">Contact:</p>
    <p class="contact__name">Marta Lindqvist</p>
    <p class="contact__line"><svg viewBox="0 0 8 8"><rect x=".5" y="1.5" width="7" height="5" fill="none" stroke="var(--ink-soft)"/><path d="M.5,1.5 L4,4.5 L7.5,1.5" fill="none" stroke="var(--ink-soft)"/></svg>info@thequietmeadownest.example</p>
    <p class="contact__line"><svg viewBox="0 0 8 8"><circle cx="4" cy="4" r="3.5" fill="none" stroke="var(--ink-soft)"/><path d="M.5,4 H7.5 M4,.5 V7.5" stroke="var(--ink-soft)" stroke-width=".7"/></svg>www.thequietmeadownest.example</p>
    <p class="contact__phone"><svg viewBox="0 0 17 14"><path d="M1,5 C1,1 16,1 16,5 L13,6 L12,4 C10,3 7,3 5,4 L4,6 Z" fill="var(--paper)"/><path d="M4,7 H13 L15,13 H2 Z" fill="var(--paper)"/></svg>+34 612 384 570</p>
  </div>
</section>

</body>
</html>
```